Business Card Design

I give lessons and clinics for dressage riders
I would like the design to be an outline (with broad lines) of a dressage horse and rider with in background of whole card with print over top tan or parchment card with burgundy print

Industry/Entity Type

Business

Contact Information for Business Card

Ned Carrow
617-354-2790
Classical dressage training for the modern American
Clinics, lessons, training level -Prix St. George

Requirements
Must have
• broad lined outline of dressage horse and rider

```html
<!DOCTYPE html>
<html lang="en">
<head>
<meta charset="utf-8">
<title>Ned Carrow – Dressage Business Card</title>
<link rel="stylesheet" href="https://fonts.googleapis.com/css2?family=Cinzel:wght@400&family=Jost:wght@400&display=swap">
<style>
  :root {
    --backdrop: #e9e9ea;
    --card-brown: #331d12;
    --figure-brown: #26140b;
    --ink-cream: #f7f1ea;
  }
  * { margin: 0; padding: 0; box-sizing: border-box; }
  html, body {
    width: 1200px;
    height: 864px;
    overflow: hidden;
    background: var(--backdrop);
  }
  .business-card {
    position: absolute;
    left: 100px;
    top: 146px;
    width: 1000px;
    height: 572px;
    background: var(--card-brown);
    color: var(--ink-cream);
    overflow: hidden;
  }
  .horse-rider-figure {
    position: absolute;
    left: 185px;
    top: 60px;
    width: 610px;
    height: 495px;
    border-radius: 46% 40% 30% 34% / 38% 42% 40% 36%;
    background: radial-gradient(ellipse at 50% 48%, var(--figure-brown) 0%, var(--figure-brown) 55%, rgba(38,20,11,0.55) 80%, rgba(51,29,18,0) 100%);
  }
  .card-text {
    position: relative;
    text-align: center;
    font-family: "Jost", "Futura", sans-serif;
    font-weight: 400;
  }
  .trainer-name {
    font-family: "Cinzel", "Trajan Pro", serif;
    font-weight: 400;
    font-size: 46px;
    letter-spacing: 2px;
    padding-top: 56px;
    line-height: 1.1;
  }
  .trainer-phone {
    font-size: 27px;
    letter-spacing: 0.5px;
    margin-top: 20px;
  }
  .tagline {
    font-size: 30px;
    line-height: 1.17;
    margin-top: 116px;
  }
  .services {
    list-style: none;
    font-size: 30px;
    line-height: 1.33;
    margin-top: 14px;
  }
</style>
</head>
<body>
  <section class="business-card">
    <div class="horse-rider-figure" role="img" aria-label="Broad-lined outline of a dressage horse and rider, printed faintly across the card background"></div>
    <div class="card-text">
      <h1 class="trainer-name">Ned Carrow</h1>
      <p class="trainer-phone">617-354-2790</p>
      <p class="tagline">Classical dressage training for the<br>modern American Clinics</p>
      <ul class="services">
        <li>lessons</li>
        <li>training level</li>
        <li>Prix St. George</li>
      </ul>
    </div>
  </section>
</body>
</html>
```